Creative Businesss Card desgin!

Create a business card for our business Gleam window cleaning!
We are open to creative ideas as long as it maintains a professional image.

Target Market(s)

Small Commercial window cleaning clients including car dealerships, strata manager, cafe

Industry/Entity Type

Window Cleaning

Contact Information for Business Card

Daniel Prescott
General Manager
Gleam Window Cleaning

daniel@gleamservices.com.au
pane-care-southbank.com.au
Ph: 1800 GET GLEAM
Mob: 0437 582 061

Colors
fbed22
0392cd

Requirements
Should not have
• Stock window cleaning/ squeegee graphics

```html
<!DOCTYPE html>
<html lang="en">
<head>
<meta charset="utf-8">
<title>Gleam Window Cleaning – Business Card</title>
<link rel="stylesheet" href="https://fonts.googleapis.com/css2?family=Arimo:wght@400;700&family=PT+Sans:ital@0;1&display=swap">
<style>
  :root {
    --brand-blue: #0392cd;
    --brand-blue-light: #3fa7da;
    --brand-yellow: #fbed22;
    --ink: #111111;
    --paper: #ffffff;
    --backdrop: #eceae6;
  }
  * { margin: 0; padding: 0; box-sizing: border-box; }
  html, body {
    width: 1200px; height: 960px; overflow: hidden;
    background: var(--backdrop);
  }
  .sheet {
    width: 1200px; height: 960px;
    display: flex; flex-direction: column; align-items: center; justify-content: center;
    gap: 40px;
  }
  .card {
    position: relative;
    width: 700px; height: 400px;
    box-shadow: 0 6px 18px rgba(0,0,0,0.18);
    overflow: hidden;
  }
  .card-shapes { position: absolute; inset: 0; }
  .card--back { background: var(--brand-blue-light); }
  .card--front { background: var(--paper); }

  .wordmark {
    position: absolute;
    color: var(--brand-yellow);
    font-family: "Arimo", Arial, sans-serif;
    font-weight: 700;
    text-align: center;
    line-height: 1;
  }
  .wordmark__name { display: block; letter-spacing: 2px; }
  .wordmark__tag { display: block; letter-spacing: 1px; }

  .card--back .wordmark { left: 0; right: 0; top: 145px; }
  .card--back .wordmark__name { font-size: 72px; }
  .card--back .wordmark__tag { font-size: 22px; margin-top: 8px; }

  .card--front .wordmark { left: 470px; width: 230px; top: 38px; }
  .card--front .wordmark__name { font-size: 56px; }
  .card--front .wordmark__tag { font-size: 17px; margin-top: 8px; }

  .person { position: absolute; left: 40px; top: 42px; font-family: "Arimo", Arial, sans-serif; }
  .person__name { font-size: 32px; line-height: 1; color: var(--ink); white-space: nowrap; }
  .person__first { color: var(--brand-blue); font-weight: 400; }
  .person__last { font-weight: 700; }
  .person__rule {
    position: absolute; left: -40px; top: 38px; width: 410px; height: 2px;
    background: var(--brand-blue);
  }
  .person__title { margin-top: 12px; font-size: 14px; color: var(--ink); letter-spacing: 0.3px; }

  .contacts {
    position: absolute; left: 40px; top: 168px;
    list-style: none;
    font-family: "PT Sans", "Myriad Pro", sans-serif;
    font-size: 18px; color: var(--ink);
  }
  .contacts__item { display: flex; align-items: center; height: 30px; }
  .contacts__icon { width: 16px; height: 16px; margin-right: 16px; flex: none; }
</style>
</head>
<body>
<main class="sheet">

  <section class="card card--back" aria-label="Card back">
    <svg class="card-shapes" width="700" height="400" viewBox="0 0 700 400" aria-hidden="true">
      <path d="M0 0 H700 V30 H330 Q318 30 312 22 L306 14 Q302 8 292 8 H0 Z" fill="var(--brand-yellow)"/>
      <path d="M0 370 H370 Q382 370 388 378 L394 386 Q398 392 408 392 H700 V400 H0 Z" fill="var(--brand-yellow)"/>
    </svg>
    <div class="wordmark">
      <span class="wordmark__name">GLEAM</span>
      <span class="wordmark__tag">WINDOW CLEANING</span>
    </div>
  </section>

  <section class="card card--front" aria-label="Card front">
    <svg class="card-shapes" width="700" height="400" viewBox="0 0 700 400" aria-hidden="true">
      <path d="M0 0 H700 V150 H488 Q472 150 464 134 L414 30 Q408 18 394 18 H0 Z" fill="var(--brand-blue)"/>
      <path d="M0 338 H220 Q232 338 238 346 L244 356 Q248 364 262 364 H700 V400 H0 Z" fill="var(--brand-blue)"/>
    </svg>

    <div class="wordmark">
      <span class="wordmark__name">GLEAM</span>
      <span class="wordmark__tag">WINDOW CLEANING</span>
    </div>

    <div class="person">
      <p class="person__name"><span class="person__first">DANIEL</span> <span class="person__last">PRESCOTT</span></p>
      <span class="person__rule"></span>
      <p class="person__title">GENERAL MANAGER</p>
    </div>

    <ul class="contacts">
      <li class="contacts__item">
        <svg class="contacts__icon" viewBox="0 0 24 24" aria-hidden="true"><path fill="var(--brand-blue)" d="M6.6 10.8a15 15 0 0 0 6.6 6.6l2.2-2.2c.3-.3.7-.4 1-.2 1.1.4 2.3.6 3.6.6.6 0 1 .4 1 1V20c0 .6-.4 1-1 1A17 17 0 0 1 3 4c0-.6.4-1 1-1h3.5c.6 0 1 .4 1 1 0 1.3.2 2.5.6 3.6.1.3 0 .7-.2 1z"/></svg>
        1800 GET GLEAM
      </li>
      <li class="contacts__item">
        <svg class="contacts__icon" viewBox="0 0 24 24" aria-hidden="true"><path fill="var(--brand-blue)" d="M6.6 10.8a15 15 0 0 0 6.6 6.6l2.2-2.2c.3-.3.7-.4 1-.2 1.1.4 2.3.6 3.6.6.6 0 1 .4 1 1V20c0 .6-.4 1-1 1A17 17 0 0 1 3 4c0-.6.4-1 1-1h3.5c.6 0 1 .4 1 1 0 1.3.2 2.5.6 3.6.1.3 0 .7-.2 1z"/></svg>
        0437 582 061
      </li>
      <li class="contacts__item">
        <svg class="contacts__icon" viewBox="0 0 24 24" aria-hidden="true"><path fill="var(--brand-blue)" d="M2 5h20v14H2z"/><path d="M2 5l10 8 10-8" fill="none" stroke="#fff" stroke-width="1.6"/></svg>
        daniel@gleamservices.com.au
      </li>
      <li class="contacts__item">
        <svg class="contacts__icon" viewBox="0 0 24 24" aria-hidden="true"><g fill="none" stroke="var(--brand-blue)" stroke-width="1.6"><circle cx="12" cy="12" r="10"/><ellipse cx="12" cy="12" rx="4.5" ry="10"/><path d="M2 12h20M4 7h16M4 17h16"/></g></svg>
        pane-care-southbank.com.au
      </li>
      <li class="contacts__item">
        <svg class="contacts__icon" viewBox="0 0 24 24" aria-hidden="true"><path fill="var(--brand-blue)" d="M12 2a7 7 0 0 0-7 7c0 5.2 7 13 7 13s7-7.8 7-13a7 7 0 0 0-7-7zm0 9.5A2.5 2.5 0 1 1 12 6.5a2.5 2.5 0 0 1 0 5z"/></svg>
        1204/38 Harbour Rd&nbsp; Southbank VIC 3006
      </li>
    </ul>
  </section>

</main>
</body>
</html>
```